Security Services Business Card

Looking for a clean modern style business card design for a residential and commercial security solutions provider. We install and service the following
security alarm, access control, video surveillance and fire alarm. Attached are the front and back of our current business cards in PSD file format.

Target Market(s)

Security alarm clients in the commercial and residential markets

Industry/Entity Type

Security Service

Contact Information for Business Card

We are open to designers suggestion and or design ideas.

Font styles to use
Serif
Sans Serif

Colors
3276b5
33a6d7
fffefd

Requirements
Must have
• Must have company logo , first and last name , phone number , web and email address, ect....

```html
<!DOCTYPE html>
<html lang="en">
<head>
<meta charset="utf-8">
<title>Veltrona Systems Business Card</title>
<link rel="stylesheet" href="https://fonts.googleapis.com/css2?family=Lato:wght@400;700&family=Roboto:wght@400;700&family=Saira+Semi+Condensed:wght@500&display=swap">
<style>
  :root {
    --backdrop: #6e6a6b;
    --navy-front: #1f3a74;
    --navy-back: #24418a;
    --sky: #33a6d7;
    --brand-blue: #2a4a9a;
    --paper: #fffefd;
    --icon-line: #8fb4e6;
  }
  * { margin: 0; padding: 0; box-sizing: border-box; }
  html, body { width: 1200px; height: 1200px; overflow: hidden; }
  body { background: var(--backdrop); position: relative; font-family: "Roboto", sans-serif; }

  .card { position: absolute; border-radius: 24px; overflow: hidden; }

  /* Front */
  .card-front { left: 238px; top: 118px; width: 712px; height: 418px; background: var(--navy-front); }
  .front-photo {
    position: absolute; left: 360px; top: 40px; width: 340px; height: 360px;
    background: radial-gradient(ellipse at 45% 40%, rgba(70,100,170,0.55), rgba(31,58,116,0) 65%);
  }
  .front-wordmark {
    position: absolute; left: 0; right: 0; top: 130px; text-align: center;
    font-family: "Roboto", sans-serif; font-weight: 700; font-size: 68px;
    color: var(--paper); letter-spacing: 1px;
  }
  .services { position: absolute; left: 52px; top: 300px; display: flex; align-items: flex-end; }
  .service { display: flex; flex-direction: column; align-items: center; padding: 0 18px; }
  .service svg { width: 44px; height: 44px; margin-bottom: 8px; }
  .service-label { font-family: "Lato", sans-serif; font-size: 17px; color: var(--paper); white-space: nowrap; }
  .divider { width: 1px; height: 62px; background: var(--icon-line); opacity: 0.7; }
  .service:first-child { padding-left: 18px; }

  /* Back */
  .card-back { left: 231px; top: 645px; width: 710px; height: 415px; background: var(--navy-back); }
  .back-shape { position: absolute; inset: 0; }
  .holder { position: absolute; left: 57px; top: 66px; color: var(--paper); }
  .holder-name { font-family: "Saira Semi Condensed", sans-serif; font-weight: 500; font-size: 29px; line-height: 36px; }
  .holder-title { font-size: 17px; line-height: 24px; margin-top: 2px; }
  .contacts { position: absolute; left: 57px; top: 208px; color: var(--paper); font-size: 18px; list-style: none; }
  .contacts li { display: flex; align-items: center; height: 26px; }
  .contacts svg { width: 16px; height: 16px; margin-right: 20px; }
  .address { position: absolute; left: 57px; top: 294px; color: var(--paper); font-size: 18px; line-height: 26px; font-style: normal; }
  .back-wordmark {
    position: absolute; left: 585px; top: 207px; width: 0; height: 0;
  }
  .back-wordmark span {
    position: absolute; transform: translate(-50%, -50%) rotate(-90deg);
    font-family: "Roboto", sans-serif; font-weight: 700; font-size: 50px;
    color: var(--brand-blue); white-space: nowrap;
  }
</style>
</head>
<body>

<section class="card card-front" aria-label="Business card front">
  <div class="front-photo" role="img" aria-label="Faint photo of a security camera mounted on a wall"></div>
  <div class="front-wordmark">Veltrona Systems</div>
  <div class="services">
    <div class="service">
      <svg viewBox="0 0 44 44" fill="none" stroke="var(--icon-line)" stroke-width="1.6" aria-hidden="true">
        <rect x="6" y="10" width="24" height="11" rx="2" transform="rotate(12 18 15)"/>
        <rect x="30" y="14" width="6" height="8"/>
        <path d="M20 24 L22 32 M14 32 H30 M34 28 V38"/>
      </svg>
      <span class="service-label">Video Surveillance</span>
    </div>
    <span class="divider"></span>
    <div class="service">
      <svg viewBox="0 0 44 44" fill="none" stroke="var(--icon-line)" stroke-width="1.6" aria-hidden="true">
        <path d="M22 4 L38 10 V22 C38 32 30 38 22 41 C14 38 6 32 6 22 V10 Z"/>
        <circle cx="22" cy="22" r="8"/>
        <path d="M18 22 L21 25 L26 19"/>
      </svg>
      <span class="service-label">Security Alarm</span>
    </div>
    <span class="divider"></span>
    <div class="service">
      <svg viewBox="0 0 44 44" fill="none" stroke="var(--icon-line)" stroke-width="1.6" aria-hidden="true">
        <path d="M12 36 V24 A10 10 0 0 1 32 24 V36"/>
        <rect x="8" y="36" width="28" height="5"/>
        <path d="M22 4 V9 M8 12 L11 15 M36 12 L33 15 M22 26 V32"/>
      </svg>
      <span class="service-label">Fire Alarm</span>
    </div>
    <span class="divider"></span>
    <div class="service">
      <svg viewBox="0 0 44 44" fill="none" stroke="var(--icon-line)" stroke-width="1.6" aria-hidden="true">
        <path d="M10 30 V20 A12 12 0 0 1 34 20 V30"/>
        <path d="M15 34 V20 A7 7 0 0 1 29 20 V34"/>
        <path d="M20 38 V20 A2 2 0 0 1 24 20 V38"/>
      </svg>
      <span class="service-label">Access Control</span>
    </div>
  </div>
</section>

<section class="card card-back" aria-label="Business card back">
  <svg class="back-shape" viewBox="0 0 710 415" aria-hidden="true">
    <path d="M454 0 C390 110 385 300 432 415 L453 415 C405 300 412 110 470 0 Z" fill="var(--sky)"/>
    <path d="M462 0 C400 110 395 300 440 415 L710 415 L710 0 Z" fill="var(--paper)"/>
  </svg>
  <div class="holder">
    <div class="holder-name">Dana Lee Morgan</div>
    <div class="holder-title">Managing Director</div>
  </div>
  <ul class="contacts">
    <li>
      <svg viewBox="0 0 16 16" fill="var(--paper)" aria-hidden="true"><path d="M1 5 C1 2 15 2 15 5 L12 7 L11 5 H5 L4 7 Z M3 8 H13 V14 H3 Z"/></svg>
      (555) 214-7390
    </li>
    <li>
      <svg viewBox="0 0 16 16" fill="none" stroke="var(--paper)" stroke-width="1.6" aria-hidden="true"><rect x="1" y="3" width="14" height="10"/><path d="M1 3 L8 9 L15 3"/></svg>
      info@veltronainfo.com
    </li>
    <li>
      <svg viewBox="0 0 16 16" fill="none" stroke="var(--paper)" stroke-width="1.4" aria-hidden="true"><circle cx="8" cy="8" r="6.5"/><ellipse cx="8" cy="8" rx="3" ry="6.5"/><path d="M1.5 8 H14.5"/></svg>
      www.veltronainfo.com
    </li>
  </ul>
  <address class="address">4810 Harbor Crest Suite #212<br>Lakewood Falls, Ohio 44000</address>
  <div class="back-wordmark"><span>Veltrona Systems</span></div>
</section>

</body>
</html>
```